Design the bid manual for Verdant Towns Congress 2019

This word document needs a makeover into an attractive brochure/manual.
All the text is there and we can send over more photos but it needs an attractive new layout and design. So essentially we need the document to be turned into a brochure that we can send via print or put online for prospective conference bidders to download and review when they put together their bid for Verdant Towns Congress 2019.

Target Market(s)

cities around the world who what to host Verdant Towns Congress, the longest running conference series on ecological cities

Font styles to use
Sans Serif

Colors
33b8a4
33a6d7
3176b5
abd037
fbed22

Requirements
Must have
• The text within the Word doc for this project.
• A bold/exciting presentation.
Nice to have
• Lots of visuals.
• here is a link to a dropbox with photos - some won't be applicable and will try and add others from past conferences
• https://www.filecrate-share.net/f/9kq2mzrt5wpl/BXRnQ7fLcH3VdYs8KeJ0uWaNm?v=0
Should not have
• stock photos

```html
<!DOCTYPE html>
<html lang="en">
<head>
<meta charset="utf-8">
<title>Verdant Towns Congress 2019 – Bid Manual</title>
<link rel="stylesheet" href="https://fonts.googleapis.com/css2?family=Lora:wght@400;500;600&family=Open+Sans:wght@400;600;700&family=Arimo:wght@400;700&display=swap">
<style>
  :root {
    --backdrop: #000000;
    --paper: #ffffff;
    --teal: #33b8a4;
    --sky: #33a6d7;
    --blue: #3176b5;
    --lime: #abd037;
    --sun: #fbed22;
    --title-ink: #3176b5;
    --sub-ink: #1f8f7e;
    --ink: #2e2e2e;
    --band-text: #ffffff;
  }
  * { margin: 0; padding: 0; box-sizing: border-box; }
  html, body { width: 999px; height: 1200px; overflow: hidden; background: var(--backdrop); }
  .spread { position: relative; width: 999px; height: 1200px; }
  .page {
    position: absolute; width: 394px; height: 557px; background: var(--paper);
    padding: 40px 28px 0 35px; color: var(--ink); overflow: hidden;
    font-family: "Open Sans", Arial, sans-serif; font-size: 9.4px; line-height: 11.4px;
  }
  .page::before {
    content: ""; position: absolute; left: 0; top: 0; width: 6px; height: 100%;
    background: linear-gradient(180deg, var(--sun), var(--lime) 30%, var(--teal) 60%, var(--sky) 80%, var(--blue));
  }
  .page--contents { left: 93px; top: 30px; }
  .page--info { left: 512px; top: 30px; font-family: "Arimo", Arial, sans-serif; }
  .page--history { left: 93px; top: 613px; padding-top: 44px; }
  .page--worldwide { left: 506px; top: 613px; padding-top: 44px; }
  .page-footer {
    position: absolute; left: 0; right: 0; bottom: 0; height: 22px;
    background: linear-gradient(90deg, var(--blue), var(--sky) 55%, var(--teal));
    border-top: 3px solid var(--lime);
    color: var(--band-text); font-family: "Open Sans", Arial, sans-serif; font-size: 10px; font-weight: 600;
    display: flex; justify-content: space-between; align-items: center; padding: 0 38px 0 34px;
  }
  .title-major {
    font-family: "Lora", Georgia, serif; font-weight: 600; color: var(--title-ink);
    font-size: 18.5px; line-height: 22px; letter-spacing: 0.2px;
  }
  .title-section {
    font-family: "Lora", Georgia, serif; font-weight: 600; color: var(--title-ink);
    font-size: 12.6px; line-height: 18px; margin: 18px 0 9px; white-space: nowrap;
  }
  .title-sub {
    font-family: "Lora", Georgia, serif; font-weight: 600; color: var(--sub-ink);
    font-size: 14px; line-height: 18px; margin: 0 0 8px; white-space: nowrap;
  }
  p.body { text-align: justify; margin-bottom: 11px; }
  .page--info .title-major { margin-bottom: 8px; }
  .page--history p.body, .page--worldwide p.body { font-size: 8.6px; line-height: 10.6px; margin-bottom: 9px; letter-spacing: -0.18px; }
  .contents-intro { font-size: 9.6px; margin: 6px 0 4px -3px; }
  .contents-item { display: grid; grid-template-columns: 41px 1fr; margin-bottom: 10px; font-size: 9.6px; line-height: 11.6px; }
  .contents-item .num { margin-left: -4px; color: var(--blue); font-weight: 700; }
  .contents-item .desc { text-align: justify; }
  .contents-item strong { font-weight: 700; color: var(--blue); }
  .contents-item .pg { font-weight: 700; color: var(--sub-ink); }
  .sub-list { list-style: none; margin-top: 1px; }
  .sub-list li { display: grid; grid-template-columns: 34px 1fr auto; line-height: 13.2px; }
  .lead-in { font-family: "Arimo", Arial, sans-serif; font-weight: 700; font-size: 8.8px; margin: 8px 0 12px; }
  .summit-list { display: grid; grid-template-columns: 182px 1fr; font-family: "Arimo", Arial, sans-serif; font-size: 8.8px; line-height: 11.4px; margin-bottom: 14px; list-style: none; padding-left: 4px; }
  .summit-list li { display: flex; align-items: center; gap: 8px; }
  .summit-list svg { flex: none; }
  .indent { text-indent: 30px; }
  .objective-label { font-family: "Arimo", Arial, sans-serif; font-weight: 700; font-size: 8.8px; margin-bottom: 6px; color: var(--blue); }
</style>
</head>
<body>
<div class="spread">

  <section class="page page--contents">
    <h1 class="title-major">CONTENTS</h1>
    <p class="contents-intro">This document is divided into three main sections:</p>

    <div class="contents-item">
      <span class="num">1.</span>
      <div class="desc">
        <strong>INFORMATION.</strong> Background on the Verdant Towns Congress ……………………………………………………………………<span class="pg">Page 4</span>
        <ul class="sub-list">
          <li><span>a.</span><span>What is the Verdant Towns Congress?</span><span class="pg">4</span></li>
          <li><span>b.</span><span>Verdant Towns Worldwide</span><span class="pg">7</span></li>
          <li><span>c.</span><span>Organization</span><span class="pg">10</span></li>
          <li><span>d.</span><span>Costs &amp; Finances</span><span class="pg">12</span></li>
          <li><span>e.</span><span>Delegates and Other Important Facts</span><span class="pg">13</span></li>
        </ul>
      </div>
    </div>

    <div class="contents-item">
      <span class="num">2.</span>
      <div class="desc">
        <strong>APPLICATION QUESTIONS AND REQUIREMENTS.</strong> The “Verdant Towns Congress conditions and questions” section details quality assurances that we expect bidders to comply with and the conditions that the host and organizer agree to uphold. The questions are designed to elicit your ideas, innovations and imagination on all aspects of event planning………………………………………<span class="pg">Page 15</span>
      </div>
    </div>

    <div class="contents-item">
      <span class="num">3.</span>
      <div class="desc">
        <strong>REQUIREMENTS AND CRITERIA.</strong> This section includes the requirements for a bid and the criteria on which a bid will be evaluated. ……………………………………… <span class="pg">Page 20</span>
        <ul class="sub-list">
          <li><span>a.</span><span>Written Bid Material</span><span class="pg">20</span></li>
          <li><span>b.</span><span>Criteria for the Choice of Venue</span><span class="pg">20</span></li>
          <li><span>c.</span><span>Decision Making</span><span class="pg">21</span></li>
          <li><span>d.</span><span>Contract</span><span class="pg">21</span></li>
          <li><span>e.</span><span>Financial</span><span class="pg">22</span></li>
          <li><span>f.</span><span>Timetable for Proposals</span><span class="pg">23</span></li>
          <li><span>g.</span><span>Final Remarks</span><span class="pg">24</span></li>
        </ul>
      </div>
    </div>

    <footer class="page-footer"><span>Verdant Towns Congress 2019</span><span>Bid Manual</span></footer>
  </section>

  <section class="page page--info">
    <h1 class="title-major">1. INFORMATION</h1>
    <p class="body">Greenhaven Builders now invites expressions of interest from those wishing to bid for hosting the next Verdant Towns Congress after the event planned for Melbourne, Australia, July 12th through 14th, 2017. Greenhaven Builders will select the city from among applicants we believe is most harmonious with the mission of the conference series as follows: to promote the understanding and development of cities that are ecologically healthy and sustainable, economically prosperous and fair, and socially just and caring.</p>
    <p class="body">Traditionally our conferences have been held every two years. The next conference will be held in 2019. This document contains the full bid manual including information required of bidders.</p>
    <h2 class="title-section">1.1. WHAT IS THE VERDANT TOWNS CONGRESS?</h2>
    <p class="body">The term "ecocity" (alternately "eco-city") was introduced by Greenhaven Builders' founder Tomas Elwood in 1979. The term is now in common use in much of the world. "Sustainable city" and "green city" are popular as well. In our tradition of drawing directly from basic life principles for the design and organization of cities, the conference series has stayed committed to "eco" because the prefix is derived from "ecology," the science of life and living systems on our planet.</p>
    <p class="body">The Verdant Towns Congress, previously known as the International Verdant Towns Conference Series (IVTCS), was the first and is now the world's longest running conference for ecological city design, development and functioning. From the beginning of planning the first conference in 1990 we have been committed to being the premier forum for leading innovative ideas, designs, policies and education about cities in balance with living systems. For twenty-six years Verdant Towns Congress has been the vanguard conference on urban issues and solutions regarding climate change, renewable energy, non-car transportation, environmentally healthy architecture and city layout. We are also leaders in issues of democratic participation in the decision making process for how we live in our built communities.</p>
    <footer class="page-footer"><span>Verdant Towns Congress 2019</span><span>Bid Manual</span></footer>
  </section>

  <section class="page page--history">
    <h2 class="title-sub">Past Verdant Towns Congresses</h2>
    <p class="lead-in">The series to date has been held in this sequence:</p>
    <ul class="summit-list">
      <li><svg width="5" height="7" viewBox="0 0 5 7"><path d="M0 0L5 3.5L0 7Z" fill="#33b8a4"/></svg>1990 Berkeley, California</li>
      <li><svg width="5" height="7" viewBox="0 0 5 7"><path d="M0 0L5 3.5L0 7Z" fill="#33b8a4"/></svg>2008 San Francisco, California</li>
      <li><svg width="5" height="7" viewBox="0 0 5 7"><path d="M0 0L5 3.5L0 7Z" fill="#33b8a4"/></svg>1992 Adelaide, Australia</li>
      <li><svg width="5" height="7" viewBox="0 0 5 7"><path d="M0 0L5 3.5L0 7Z" fill="#33b8a4"/></svg>2009 Istanbul, Turkey,</li>
      <li><svg width="5" height="7" viewBox="0 0 5 7"><path d="M0 0L5 3.5L0 7Z" fill="#33b8a4"/></svg>1996 Yoff and Dakar, Senegal</li>
      <li><svg width="5" height="7" viewBox="0 0 5 7"><path d="M0 0L5 3.5L0 7Z" fill="#33b8a4"/></svg>2011 Montreal, Canada</li>
      <li><svg width="5" height="7" viewBox="0 0 5 7"><path d="M0 0L5 3.5L0 7Z" fill="#33b8a4"/></svg>2000 Curitiba, Brazil</li>
      <li><svg width="5" height="7" viewBox="0 0 5 7"><path d="M0 0L5 3.5L0 7Z" fill="#33b8a4"/></svg>2013 Nantes, France</li>
      <li><svg width="5" height="7" viewBox="0 0 5 7"><path d="M0 0L5 3.5L0 7Z" fill="#33b8a4"/></svg>2002 Shenzhen, China</li>
      <li><svg width="5" height="7" viewBox="0 0 5 7"><path d="M0 0L5 3.5L0 7Z" fill="#33b8a4"/></svg>2015 Abu Dhabi, UAE</li>
      <li><svg width="5" height="7" viewBox="0 0 5 7"><path d="M0 0L5 3.5L0 7Z" fill="#33b8a4"/></svg>2006 Bangalore, India</li>
      <li><svg width="5" height="7" viewBox="0 0 5 7"><path d="M0 0L5 3.5L0 7Z" fill="#33b8a4"/></svg>2017 Melbourne, Australia</li>
    </ul>
    <p class="body indent">We continue to be the unique conference series to feature a broad spectrum of presenters and participants — from architects and planners to environmentalists and developers; from alternative energy pioneers and transportation advocates to government officials and artists supporting and enriching the lives of all citizens. With our education and research emphasis we have provided a forum for scientists and philosophers, professors and early-learning professionals, writers and journalists, and even an astronaut who walked on the moon. Legislators and green business people of a wide variety of ventures, indigenous peoples and minorities, and historic preservationists and futurists have all been represented.</p>
    <p class="body">What inspires our emphasis on representing this complex network is the fact that cities are whole systems. Only when all of its parts are working together can we steadily improve the health and wellbeing of the whole.</p>
    <h2 class="title-sub" style="margin-top:12px">1.1.1. Objectives of the Verdant Towns Congress</h2>
    <p class="objective-label">1. Cities becoming ecocities</p>
    <p class="body">The major objective of the conference series is to promote healthy cities in all their aspects for long-term vitality of living systems. In addition to natural systems these include human social systems: political, economic, cultural and social.</p>
    <p class="body">The Verdant Towns Congress showcases the “new towns” approach and the “transform existing cities” approach that aspire to meet ecologically healthy, socially fair and equitable goals. We emphasize that we seek not to support random technologies, practices and policies out of context with their built and natural environments; instead we promote approaches that fundamentally address basic principles for healthy whole-systems transformation. In other words, we seek solutions in design and layout as well as in technologies and lifestyles, the whole built and natural environment and its constituent parts harmonized.</p>
    <footer class="page-footer"><span>Verdant Towns Congress 2019</span><span>Bid Manual</span></footer>
  </section>

  <section class="page page--worldwide">
    <h2 class="title-sub">2. Cutting across scales, systems and particulars</h2>
    <p class="body">We seek solutions over all scales, from the single technological item that may contribute to healthier built communities to the whole system, from the small Ecovillage and Ecotown to the Ecocity and Ecotropolis becoming more harmonious with its bioregion and the planet. The term Ecocity is becoming the generic for ecologically healthy total built community at all scales.</p>
    <h2 class="title-sub" style="margin-top:12px">3. Connecting people with Ecocity knowledge</h2>
    <p class="body">The conferences series also aspires to provide the best information among its participants relative to their interests and to connect people of a wide variety of kindred disciplines and cross-cutting projects associated with the conference’s major themes. In our case, our chief objective is to facilitate outcomes, including new and refreshed partnerships and collaborations that help build and run the healthy city of the future.</p>
    <h2 class="title-sub" style="margin-top:12px">4. Promoting the host city</h2>
    <p class="body">Also importantly, the conference series serves to spotlight the best in the ecocity offerings of the host city and to bring them enhanced success in their relevant work.</p>
    <h2 class="title-section" style="margin-top:10px;font-size:14px">1.2. VERDANT TOWNS WORLDWIDE</h2>
    <p class="body">Greenhaven Builders seeks conference hosts who agree that we need both bottom-up and top-down approaches to solving our urban and environmental problems and are dedicated to representing this in the programming of the event. We have been a conference series with a very international, multi-cultural and social justice-oriented set of events that go to very particular places looking for connections. We have held these conferences on all continents except Antarctica.</p>
    <p class="body">We understand that city design, planning, building and maintaining must respond creatively, appropriately and effectively to world conditions such as climate change, resource limits, supply of healthy soil, water and bioregional “ecological services.” This means balancing human settlements with the preservation of forests, grasslands, wetlands, open waters, and glaciers. We understand principles such as limits on a finite planet, ecological overshoot and the implications of the “ecological footprint.” All these concepts are basic background material to our programs and help guide our conference design and development process, selection of presenters, panelists, workshops, tours and exhibits.</p>
    <footer class="page-footer"><span>Verdant Towns Congress 2019</span><span>Bid Manual</span></footer>
  </section>

</div>
</body>
</html>
```